GreyHeron Contractors - Application form

I have an old application form in an editable PDF format (attached) which needs updating and bringing into the new branding. I would like both a word and editable PDF version of the application form

Target Market(s)

Contractors who are looking to join and use our umbrella services

Requirements
Must have
• All fields in the attached PDF version.
• Inline with the look and feel of the logo and web design attached.

```html
<!DOCTYPE html>
<html lang="en">
<head>
<meta charset="utf-8">
<title>GreyHeron Contractors – Application Form</title>
<link href="https://fonts.googleapis.com/css2?family=Roboto:wght@400;500;700&display=swap" rel="stylesheet">
<style>
  :root{
    --backdrop:#ececec;
    --paper:#f4f4f4;
    --charcoal:#3a3a3a;
    --panel-grey:rgba(105,108,112,0.85);
    --field-light:#f4f4f4;
    --field-edge:#8a8a8a;
    --ink:#222222;
    --ink-inverse:#ffffff;
  }
  *{box-sizing:border-box;margin:0;padding:0}
  html,body{width:1200px;height:1200px;overflow:hidden;background:var(--backdrop);font-family:"Roboto",Arial,sans-serif}
  .sheet{position:absolute;left:195px;top:15px;width:880px;height:1272px;background:var(--paper);transform:scale(0.92);transform-origin:top left;overflow:hidden}
  .hero{position:absolute;left:0;top:0;width:880px;height:237px;background:linear-gradient(100deg,#eef1f4 0%,#cfd8e1 35%,#b9c6d3 60%,#dfe5ea 100%)}
  .brand{position:absolute;left:46px;top:78px;width:300px;font-size:36px;font-weight:700;color:var(--charcoal);line-height:1.15}
  .brand span{display:block}
  .intro{position:absolute;left:373px;top:52px;width:507px;height:134px;background:var(--panel-grey);color:var(--ink-inverse);padding:16px 40px 16px 31px}
  .intro h1{font-size:30px;font-weight:500;margin-bottom:13px}
  .intro p{font-size:12.5px;line-height:16.5px;hyphens:auto}
  .section-dark{position:absolute;left:0;top:237px;width:880px;height:440px;background:var(--charcoal)}
  .tab{position:absolute;left:0;width:571px;height:42px;padding-left:46px;font-size:21px;font-weight:500;line-height:42px}
  .tab--light{top:265px;background:var(--paper);color:var(--ink)}
  .tab--dark{top:708px;background:var(--charcoal);color:var(--ink-inverse)}
  .label{position:absolute;font-size:12.5px;white-space:nowrap;transform:translateY(-50%)}
  .on-dark{color:var(--ink-inverse)}
  .on-light{color:var(--ink)}
  .strong{font-weight:500}
  .field{position:absolute;height:19px;background:var(--field-light);border:1px solid var(--field-edge)}
  .field--dark{background:var(--charcoal);border:none}
  .tick{position:absolute;width:19px;height:19px;background:var(--charcoal)}
  .textarea{position:absolute;left:47px;width:787px;height:84px;background:var(--charcoal)}
</style>
</head>
<body>
<main class="sheet">
  <div class="hero" role="img" aria-label="Soft-focus photograph of city office towers"></div>
  <div class="brand"><span>GreyHeron</span><span>Contractors</span></div>
  <div class="intro">
    <h1>Application Form</h1>
    <p>Please complete the form below and detail your permanent residential information as per your identification documentation. We'll start pro&shy;cessing your application straight away.</p>
  </div>

  <section class="section-dark"></section>
  <h2 class="tab tab--light">Applicant and Permanent Residential Information</h2>

  <span class="label on-dark" style="left:46px;top:346px">Title (as per identification documents):</span>
  <span class="label on-dark" style="left:310px;top:346px">Mr:</span><div class="field" style="left:338px;top:337px;width:19px"></div>
  <span class="label on-dark" style="left:394px;top:346px">Mrs:</span><div class="field" style="left:428px;top:337px;width:19px"></div>
  <span class="label on-dark" style="left:481px;top:346px">Miss:</span><div class="field" style="left:519px;top:337px;width:19px"></div>
  <span class="label on-dark" style="left:570px;top:346px">Ms:</span><div class="field" style="left:598px;top:337px;width:19px"></div>
  <span class="label on-dark" style="left:652px;top:346px">Other:</span><div class="field" style="left:696px;top:337px;width:138px"></div>

  <span class="label on-dark" style="left:46px;top:381px">Forename(s):</span><div class="field" style="left:134px;top:373px;width:278px"></div>
  <span class="label on-dark" style="left:426px;top:381px">Surname:</span><div class="field" style="left:492px;top:373px;width:341px"></div>

  <span class="label on-dark" style="left:46px;top:417px">Are you a UK resident for tax purposes?</span>
  <span class="label on-dark" style="left:317px;top:417px">Yes:</span><div class="field" style="left:349px;top:408px;width:19px"></div>
  <span class="label on-dark" style="left:426px;top:417px">No:</span><div class="field" style="left:456px;top:408px;width:19px"></div>

  <span class="label on-dark" style="left:46px;top:454px">Home Telephone:</span><div class="field" style="left:166px;top:446px;width:278px"></div>
  <span class="label on-dark" style="left:458px;top:454px">Mobile Telephone:</span><div class="field" style="left:580px;top:446px;width:253px"></div>

  <span class="label on-dark" style="left:46px;top:491px">Email Address:</span><div class="field" style="left:146px;top:482px;width:298px"></div>
  <span class="label on-dark" style="left:461px;top:491px">House Name/Number:</span><div class="field" style="left:609px;top:482px;width:224px"></div>

  <span class="label on-dark" style="left:46px;top:527px">Street/Road Name:</span><div class="field" style="left:172px;top:519px;width:661px"></div>

  <span class="label on-dark" style="left:46px;top:564px">Town/City:</span><div class="field" style="left:122px;top:556px;width:322px"></div>
  <span class="label on-dark" style="left:457px;top:564px">Country:</span><div class="field" style="left:520px;top:556px;width:313px"></div>

  <span class="label on-dark" style="left:46px;top:600px">Postcode:</span><div class="field" style="left:143px;top:592px;width:301px"></div>
  <span class="label on-dark" style="left:457px;top:600px">Nationality:</span><div class="field" style="left:537px;top:592px;width:296px"></div>

  <span class="label on-dark" style="left:46px;top:636px">Date of Birth:</span><div class="field" style="left:138px;top:628px;width:306px"></div>
  <span class="label on-dark" style="left:457px;top:636px">Your NI Number:</span><div class="field" style="left:571px;top:628px;width:262px"></div>

  <h2 class="tab tab--dark">Applicant and Permanent Residential Information</h2>

  <span class="label on-light" style="left:47px;top:791px">Industry Sector:</span><div class="field field--dark" style="left:152px;top:784px;width:268px"></div>
  <span class="label on-light" style="left:433px;top:791px">Job Title:</span><div class="field field--dark" style="left:500px;top:784px;width:333px"></div>

  <span class="label on-light strong" style="left:47px;top:827px">Please tick which category best describes your role:</span>
  <div class="tick" style="left:49px;top:850px"></div><span class="label on-light" style="left:77px;top:859px">Clerical - Administrative/IT</span>
  <div class="tick" style="left:289px;top:850px"></div><span class="label on-light" style="left:318px;top:859px">Clerical - Technical/Professional</span>
  <div class="tick" style="left:49px;top:881px"></div><span class="label on-light" style="left:77px;top:891px">Manual (NB: this means your role involves use of hand tools more than 20% of the time)</span>

  <span class="label on-light strong" style="left:47px;top:921px">Short description of key responsibilities (e.g. “I am responsible for designing, developing and executing test plans”):</span>
  <div class="textarea" style="top:935px"></div>

  <span class="label on-light strong" style="left:47px;top:1043px">Please list any qualifications, authorisations, experience or training requirements placed upon you by your end client,</span>
  <span class="label on-light strong" style="left:47px;top:1060px">agency or professional body to undertake your role:</span>
  <div class="textarea" style="top:1078px"></div>

  <div class="tick" style="left:49px;top:1175px"></div><span class="label on-light" style="left:80px;top:1184px">I confirm that I have all of the above and will co-operate in any checks in relation to these as required.</span>

  <span class="label on-light strong" style="left:46px;top:1213px">Does you role require you to have regular access to vulnerable adults and/or young children?</span>
  <span class="label on-light strong" style="left:665px;top:1213px">Yes:</span><div class="tick" style="left:699px;top:1203px"></div>
  <span class="label on-light strong" style="left:773px;top:1213px">No:</span><div class="tick" style="left:804px;top:1203px"></div>
  <span class="label on-light" style="left:46px;top:1236px">(If so, please provide copy of most recent DBS check.)</span>
</main>
</body>
</html>
```